Website/Logo Design

We need a logo and website design for an opinion mining startup called VantaLume. Our technology mines the web to automatically discover what people are saying about brands, products, etc. The project we are fielding here is for our informational, public-facing website. In its initial incarnation, it will simply be a vehicle for marketing materials and information on our company and its offerings, but it should be flexible enough to expand as more content/functionality is added.

Some designs we like are:
http://www.tradewhisk.example
http://www.gorvantel.example
http://www.kfz.example
http://www.lintwharf.example
http://moxbarrel.example
http://trundlemq.example
http://www.zopla.example
Updates

All, please try to shy away from using a photo of a person as the focal point of the design.  Our company is more technological than social.

Target Market(s)

Primarily businesses interested in sentiment analysis (typically companies involved in advertising, market research, PR, etc.)

Industry/Entity Type

It Company

Requirements
Must have
• We are looking for a clean, modern, and professional design. This includes a logo, homepage, and internal page if it will differ from the homepage.
Nice to have
• It would be excellent if you could provide an HTML mockup if your design is chosen.
Should not have
• Flash, excessive bells and whistles

```html
<!DOCTYPE html>
<html lang="en">
<head>
<meta charset="utf-8">
<title>VantaLume</title>
<link rel="stylesheet" href="https://fonts.googleapis.com/css2?family=Poiret+One&family=Arimo:wght@400;700&family=Tinos&display=swap">
<style>
:root{
  --teal:#0e7088;
  --teal-dark:#034656;
  --ink:#231f20;
  --sky-top:#eaf7fd;
  --sky-bottom:#c3e6f7;
  --paper:#e9e7e8;
  --white:#ffffff;
  --rule:#8a8a8a;
  --alert:#e0141b;
  --logo-grey:#9a9a9a;
}
*{margin:0;padding:0;box-sizing:border-box}
html,body{width:1200px;height:1123px;overflow:hidden}
body{position:relative;background:var(--paper);font-family:"Arimo",Arial,sans-serif;color:var(--ink)}
.abs{position:absolute}

.site-header{left:0;top:0;width:1200px;height:186px;background:linear-gradient(var(--sky-top),var(--sky-bottom))}
.brand{left:58px;top:50px;font-family:"Arimo",Arial,sans-serif;font-weight:700;font-size:62px;letter-spacing:-1px;color:var(--ink)}
.call-us{right:56px;top:8px;font-weight:700;font-size:23px;color:var(--teal);letter-spacing:.5px}
.call-tel{right:56px;top:34px;font-size:22px;color:var(--ink)}
.login-title{left:820px;top:76px;font-size:16px}
.field{top:104px;width:157px;height:25px;background:var(--white);border:1px solid #b8c4cc;font-size:12px;color:#777;padding:5px 6px}
.field.user{left:820px}
.field.pass{left:988px}
.login-btn{left:820px;top:145px;width:53px;height:25px;background:#7ec3da;border:1px solid #4a8ea6;font-size:12px;line-height:23px;text-align:center}
.login-links{left:882px;top:149px;font-size:13px;font-weight:700}
.login-links .forgot{text-decoration:underline;color:var(--ink)}
.login-links .new{color:var(--alert)}

.main-nav{left:0;top:186px;width:1200px;height:54px;background:linear-gradient(#157a92,var(--teal-dark));border-top:2px solid #7fc4d6;display:flex;justify-content:center;align-items:center;font-family:"Poiret One","Arimo",sans-serif;font-size:23px;color:var(--white);font-weight:400}
.main-nav span{padding:0 16px}

.hero{left:0;top:240px;width:1200px;height:270px;background:#000}
.hero-line{left:80px;top:50px;width:790px;text-align:center;font-family:"Poiret One",sans-serif;font-size:40px;line-height:43px;color:var(--white)}
.hero-art{left:900px;top:30px;width:150px;height:200px;background:radial-gradient(ellipse at 50% 40%,#b08a4a 0%,#4a3416 35%,#000 70%)}

.section-title{font-size:18px;font-weight:700;color:var(--ink)}
.section-title b{font-size:26px;color:var(--teal);margin-left:6px}
.rule{height:0;border-top:2px dotted var(--rule)}
.copy{font-family:Verdana,"Arimo",sans-serif;font-size:12px;line-height:21.6px;color:#111}
.read-more{font-size:13px;font-weight:700;display:flex;align-items:center;gap:5px}
.read-more i{display:inline-block;width:10px;height:10px;background:var(--teal)}

.clients{left:636px;top:809px;width:508px;height:99px;background:var(--white);display:grid;grid-template-columns:repeat(4,1fr);align-items:center;justify-items:center;padding:4px 6px}
.clients span{font-weight:700;font-size:17px;color:var(--logo-grey)}

.site-footer{left:0;top:986px;width:1200px;height:137px;background:var(--ink);color:var(--white)}
.foot-brand{left:58px;top:14px;font-family:"Tinos",serif;font-size:28px;color:var(--teal)}
.foot-address{left:64px;top:54px;font-size:14px;line-height:18px}
.foot-divider{left:226px;top:44px;height:76px;border-left:2px dotted #666}
.foot-contact{left:253px;top:52px;font-size:13px;line-height:16.5px;font-weight:700}
.foot-contact em{font-style:normal;color:var(--teal)}
.foot-links{right:56px;top:52px;font-size:13px}
.foot-links span{padding:0 6px}
.foot-copy{right:56px;top:74px;font-size:12px}
</style>
</head>
<body>

<header class="site-header abs">
  <div class="brand abs">VantaLume</div>
  <div class="call-us abs">CALL US</div>
  <div class="call-tel abs">Tel : +33(0)6 412. 507.36</div>
  <div class="login-title abs">Log&nbsp; In</div>
  <div class="field user abs">user name</div>
  <div class="field pass abs">password</div>
  <div class="login-btn abs">Log In</div>
  <div class="login-links abs"><span class="forgot">forgot your password</span> ? <span class="new">New ?</span> Sign Up</div>
</header>

<nav class="main-nav abs">
  <span>Home</span>|<span>About VantaLume</span>|<span>How We Work</span>|<span>Case Studies</span>|<span>Pricing</span>|<span>Contact</span>
</nav>

<section class="hero abs">
  <p class="hero-line abs">Our technology mines the web to automatically discover what people are saying about brands, products, etc.</p>
  <div class="hero-art abs" role="img" aria-label="Glowing light-painted question mark on black"></div>
</section>

<section class="abs" style="left:56px;top:540px;width:534px">
  <h2 class="section-title">Welcome to<b>VantaLume</b></h2>
  <div class="rule" style="margin-top:6px"></div>
  <p class="copy" style="margin-top:8px">Lorem ipsum dolor sit amet, consectetur adipiscing elit. Maecenas luctus arcu sit amet quam viverra condimentum. Suspendisse aliquam ullamcorper sapien suscipit laoreet. Suspendisse varius sodales lectus sit amet convallis. Vestibulum facilisis condimentum lorem, quis commodo tortor luctus eget.</p>
  <div class="read-more" style="margin-top:26px"><i></i>read more</div>
</section>

<section class="abs" style="left:636px;top:538px;width:508px">
  <h2 class="section-title">our<b>Services</b></h2>
  <div class="rule" style="margin-top:6px"></div>
  <p class="copy" style="margin-top:8px">Lorem ipsum dolor sit amet, consectetur adipiscing elit. Maecenas luctus arcu sit amet quam viverra condimentum. Suspendisse aliquam ullamcorper sapien suscipit laoreet. Suspendisse varius sodales lectus sit amet convallis. Vestibulum facilisis condimentum lorem, quis commodo tortor luctus eget.</p>
  <div class="read-more" style="margin-top:26px"><i></i>read more</div>
</section>

<section class="abs" style="left:56px;top:748px;width:534px">
  <h2 class="section-title">Who<b>We Are</b></h2>
  <div class="rule" style="margin-top:6px"></div>
  <p class="copy" style="margin-top:8px">Lorem ipsum dolor sit amet, consectetur adipiscing elit. Maecenas luctus arcu sit amet quam viverra condimentum. Suspendisse aliquam ullamcorper sapien suscipit laoreet. Suspendisse varius sodales lectus sit amet convallis. Vestibulum facilisis condimentum lorem, quis commodo tortor luctus eget.</p>
  <div class="read-more" style="margin-top:26px"><i></i>read more</div>
</section>

<section class="abs" style="left:636px;top:748px;width:508px">
  <h2 class="section-title">our<b>Clients</b></h2>
  <div class="rule" style="margin-top:6px"></div>
</section>
<div class="clients abs">
  <span>Quillmark</span><span>Tessaline</span><span>Norrit</span><span>Calderwise</span>
  <span>Fennick</span><span>Larch Hollow</span><span>Pell</span><span>Ostby &amp; Crane</span>
</div>

<footer class="site-footer abs">
  <div class="foot-brand abs">VantaLume</div>
  <div class="foot-address abs">17 dummy address<br>Dummy Address<br>Dummy Addrses</div>
  <div class="foot-divider abs"></div>
  <div class="foot-contact abs"><em>Tel :</em> +33(0)6 41 25 07 36<br><em>Email :</em> abcd.ab@vantalume.example<br><em>Skype :</em> noel.varga</div>
  <div class="foot-links abs"><span>Home</span>|<span>About VantaLume</span>|<span>How We Work</span>|<span>Case Studies</span>|<span>Pricing</span>|<span>Clients</span>|<span>Blogs</span>|<span style="padding-right:0">Contact Us</span></div>
  <div class="foot-copy abs">© 2010 vantalume.example | All rights reserved</div>
</footer>

</body>
</html>
```